Business card design for Summit Wallcrafters required

Our company "Boardline Finishing Harbor Works" needs business cards. Make the business cards be found easily amongst 100 other construction business cards. White background, logo centered and large.

Target Market(s)

Customers or builders who need a drywaller and customers who need a very high quality drywaller.

Industry/Entity Type

Construction

Contact Information for Business Card

The business logo centered and large with "Serving Pinehollow County 12+years" in black Italic, and 2 telephone numbers centered beneath written: Ada / Lou: 403-682-1357, and 403-739-2864 beneath. The business cards will be printed in metal with rounded corners.

Colors
ec1f27

Requirements
Must have
• The selected logo. Must be able to see "DRYWALL" from a distance. Must stick out from other business cards.

```html
<!DOCTYPE html>
<html lang="en">
<head>
<meta charset="utf-8">
<title>Boardline Finishing Harbor Works – Business Card</title>
<link href="https://fonts.googleapis.com/css2?family=Lato:ital,wght@0,300;0,400;0,700;1,700&display=swap" rel="stylesheet">
<style>
  :root {
    --page-bg: #e6e7e9;
    --card-bg: #f7f7f8;
    --card-edge: #d2d4d7;
    --brand-red: #ec1f27;
    --band-red: #c8141b;
    --band-red-dark: #9e0e13;
    --muted-grey: #8a8a8c;
    --phone-grey: #a8a8aa;
    --ink: #2a2a2a;
    --white: #ffffff;
  }
  * { box-sizing: border-box; margin: 0; padding: 0; }
  html, body {
    width: 1200px;
    height: 970px;
    overflow: hidden;
    background: var(--page-bg);
    font-family: "Lato", Arial, sans-serif;
  }
  .business-card {
    position: absolute;
    left: 100px;
    top: 184px;
    width: 1000px;
    height: 602px;
    background: var(--card-bg);
    border: 1px solid var(--card-edge);
    border-radius: 14px;
    overflow: hidden;
    box-shadow: 0 10px 30px rgba(0,0,0,0.12);
  }
  .brand {
    position: absolute;
    top: 78px;
    left: 0;
    width: 100%;
    height: 104px;
    display: flex;
    justify-content: center;
    align-items: center;
    gap: 20px;
  }
  .brand-square {
    width: 100px;
    height: 100px;
    background: var(--brand-red);
    flex: none;
  }
  .brand-name {
    font-weight: 700;
    font-size: 40px;
    line-height: 1;
    color: var(--brand-red);
    white-space: nowrap;
  }
  .contact-band {
    position: absolute;
    left: 0;
    top: 304px;
    width: 100%;
    height: 112px;
    background: linear-gradient(180deg, var(--band-red) 0%, var(--band-red-dark) 100%);
  }
  .band-slash {
    position: absolute;
    left: 0;
    top: 0;
    width: 100%;
    height: 100%;
  }
  .contact {
    position: absolute;
    top: 12px;
    width: 400px;
    text-align: center;
  }
  .contact-left { left: 107px; }
  .contact-right { left: 495px; }
  .contact-name {
    display: block;
    font-weight: 700;
    font-size: 29px;
    line-height: 1.3;
  }
  .contact-left .contact-name { color: var(--muted-grey); }
  .contact-right .contact-name { color: var(--white); }
  .contact-phone {
    display: block;
    font-weight: 400;
    font-size: 32px;
    line-height: 1.4;
    color: var(--phone-grey);
  }
  .service-line {
    position: absolute;
    top: 545px;
    left: 0;
    width: 100%;
    text-align: center;
    font-weight: 700;
    font-style: italic;
    font-size: 23px;
    line-height: 1.3;
    color: var(--ink);
  }
</style>
</head>
<body>
  <article class="business-card">
    <header class="brand">
      <div class="brand-square"></div>
      <h1 class="brand-name">Boardline Finishing Harbor Works</h1>
    </header>

    <section class="contact-band">
      <svg class="band-slash" viewBox="0 0 1000 112" preserveAspectRatio="none" aria-hidden="true">
        <line x1="551" y1="0" x2="467" y2="112" stroke="#f2f2f2" stroke-width="3" stroke-opacity="0.8"/>
      </svg>
      <div class="contact contact-left">
        <span class="contact-name">Ada:</span>
        <span class="contact-phone">403-682-1357</span>
      </div>
      <div class="contact contact-right">
        <span class="contact-name">Lou:</span>
        <span class="contact-phone">403-739-2864</span>
      </div>
    </section>

    <p class="service-line">Serving Pinehollow County 12+years</p>
  </article>
</body>
</html>
```